Home page in PSD needed for a Business Consultant website

We have been given the mandate to re-do the website: http://www.lumivanconseil.ca/

Deliverable: home page in PSD format in French language

Context: Luc Dorval is a business strategist specializing in marketing, creativity, business development. He helps small and medium companies develop their business through creative marketing strategies.

Some websites we like for your inspiration:

http://www.tallpinegrove.com.au/
http://www.trwadvisory.com.au/
http://fjalladvisors.com.au/
http://www.olubrenix.com/fr

Target Market(s)

B2B: Companies looking on the web for a business consultant who can help them with marketing, business developement, printing needs.

Industry/Entity Type

Business

Requirements
Must have
• Call to action: "Simplifiez votre développement des affaires" (which means "Simplify your business development")
• List of services (main menu)
• Marketing
• Développement des affaires
• Créativité
• Scolaire
• Impression
• Top menu as follow:
• Accueil
• À propos
• Contact

```html
<!DOCTYPE html>
<html lang="fr">
<head>
<meta charset="utf-8">
<title>Lumivan Conseil — Luc Dorval</title>
<link rel="stylesheet" href="https://fonts.googleapis.com/css2?family=Arimo:wght@400;700&family=PT+Serif:wght@400;700&display=swap">
<style>
:root{
  --blue:#0a76c4;
  --ink:#333333;
  --nav:#3a3a3a;
  --nav-active:#5a5a5a;
  --text:#555555;
  --footer:#333333;
  --footer-text:#d0d0d0;
  --white:#ffffff;
  --card:#f4f4f4;
}
*{box-sizing:border-box;margin:0;padding:0}
html,body{width:1133px;height:1200px;overflow:hidden;background:var(--white);font-family:"Arimo",Arial,sans-serif}
.page{position:relative;width:1133px;height:1200px;overflow:hidden}
.abs{position:absolute}

/* header */
.header-shapes{left:0;top:0}
.brand{left:172px;top:30px;font-family:"PT Serif",Georgia,serif;font-size:29px;color:var(--ink);display:flex;align-items:center;gap:10px;white-space:nowrap}
.brand-dot{width:14px;height:14px;border-radius:50%;background:var(--blue)}
.call{left:828px;top:13px;display:flex;gap:12px;align-items:center}
.call-icon{width:33px;height:33px;border-radius:6px;background:#dbe9f5;display:flex;align-items:center;justify-content:center}
.call-text{color:var(--white);font-weight:700;font-size:17.5px;line-height:17px}
.nav{left:527px;top:62px;height:35px;display:flex;list-style:none}
.nav li{height:35px;line-height:35px;font-size:12.5px;color:var(--white);padding:0 19px;white-space:nowrap}
.nav li.active{background:var(--nav-active)}

/* about */
.about-bg{left:0;top:97px;width:1133px;height:598px;background:linear-gradient(180deg,#fff 0%,#fff 78%,#ececec 100%)}
.hero{left:142px;top:133px;width:849px;height:307px;background:radial-gradient(ellipse at 50% 45%,#7a7a7a 0%,#3c3c3c 55%,#1e1e1e 100%);display:flex;align-items:center;justify-content:center}
.hero-cta{font-family:"PT Serif",Georgia,serif;font-weight:700;font-size:30px;color:var(--white);text-align:center;width:600px;line-height:38px;margin-right:120px}
.portrait{left:840px;top:106px;width:152px;height:567px;background:linear-gradient(180deg,#cfd2d8 0%,#8a8f9c 35%,#5d6270 100%);opacity:.55}
.about-title{left:143px;top:470px;font-family:"PT Serif",Georgia,serif;font-size:25px;color:#222;font-weight:400}
.about-title span{color:var(--blue)}
.about-copy{left:142px;top:521px;width:640px;font-size:11.6px;line-height:16px;color:var(--text);text-align:justify}
.about-copy p+p{margin-top:15px}

/* cards */
.card{top:742px;width:248px;height:239px;background:var(--card);border:1px solid #e3e3e3}
.card-media{width:100%;height:112px}
.card-title{margin:13px 11px 0;font-family:"PT Serif",Georgia,serif;font-size:15px;line-height:16px;color:var(--blue);font-weight:400}
.card-title b{font-weight:700;text-transform:uppercase}
.card-text{margin:5px 11px 0;font-size:10.5px;line-height:14px;color:var(--text);text-align:justify;letter-spacing:.2px}
.card-more{position:absolute;right:-1px;bottom:-1px;width:95px;height:22px}
.card-more span{position:absolute;left:0;top:0;width:95px;line-height:22px;text-align:right;padding-right:10px;color:var(--white);font-size:11px}

/* footer */
.footer-shapes{left:0;top:1043px}
.f-head{top:1058px;font-size:14.5px;color:var(--white)}
.f-list{list-style:none;top:1085px;font-size:10.5px;color:var(--footer-text);letter-spacing:.4px}
.f-list li{height:19.5px}
.f-row{display:flex;gap:10px;font-size:10.5px;color:var(--footer-text);letter-spacing:.3px;line-height:12.5px}
.f-row b{color:var(--white);font-weight:700}
.soc{width:20px;height:20px;background:#777}
.f-brand{left:745px;top:1105px;font-family:"PT Serif",Georgia,serif;font-size:26px;color:var(--white);display:flex;align-items:center;gap:9px;white-space:nowrap}
.f-brand .brand-dot{background:var(--white)}
.copyright{left:759px;top:1168px;font-size:10.5px;color:var(--white)}
</style>
</head>
<body>
<div class="page">

  <svg class="abs header-shapes" width="1133" height="97" viewBox="0 0 1133 97" aria-hidden="true">
    <rect width="1133" height="97" fill="#0a76c4"/>
    <polygon points="452,62 1133,62 1133,97 423,97" fill="#3a3a3a"/>
    <polygon points="155,0 487,0 423,97 88,97" fill="#ffffff"/>
  </svg>
  <div class="abs brand"><span class="brand-dot"></span>Lumivan Conseil</div>
  <div class="abs call">
    <div class="call-icon">
      <svg width="18" height="20" viewBox="0 0 18 20" aria-hidden="true"><path d="M4 1 L7 5 L5 7 C6 10 8 13 11 15 L13 13 L17 16 L15 19 C8 18 2 11 1 4 Z" fill="none" stroke="#0a76c4" stroke-width="1.8" stroke-linejoin="round"/></svg>
    </div>
    <div class="call-text">Luc Dorval<br>514 555 0192</div>
  </div>
  <ul class="abs nav">
    <li class="active">Accueil</li>
    <li>À propos</li>
    <li>Services</li>
    <li>Témoignages</li>
    <li>Contact</li>
  </ul>

  <div class="abs about-bg"></div>
  <div class="abs hero" role="img" aria-label="Croquis à la craie d'une carte de stratégie d'affaires sur fond sombre">
    <p class="hero-cta">Simplifiez votre développement des affaires</p>
  </div>
  <div class="abs portrait" role="img" aria-label="Photo du consultant debout en complet foncé"></div>
  <h1 class="abs about-title">À propos de <span>LUC DORVAL</span></h1>
  <div class="abs about-copy">
    <p>Lorem ipsum dolor sit amet, consectetur adipiscing elit. Sed placerat mauris at felis vehicula faucibus ac ac dui. Maecenas in mattis lectus. Donec gravida, purus ac lobortis condimentum, tellus justo euismod sapien, imperdiet eleifend nisl tellus sit amet lorem. Pellentesque vel suscipit arcu. Proin sollicitudin vel nunc non consequat. Maecenas dolor turpis, consequat eget adipiscing nec, sagittis sed est.</p>
    <p>Lorem ipsum dolor sit amet, consectetur adipiscing elit. Sed placerat mauris at felis vehicula faucibus ac ac dui. Maecenas in mattis lectus. Donec gravida, purus ac lobortis condimentum, tellus justo euismod sapien, imperdiet eleifend nisl tellus sit amet lorem.</p>
  </div>

  <div class="abs card" style="left:142px">
    <div class="card-media" role="img" aria-label="Carte mentale marketing dessinée sur papier avec un crayon" style="background:linear-gradient(135deg,#e8e2d6,#f7f5f0 60%,#d9d3c6)"></div>
    <h2 class="card-title"><b>Marketing</b> stratégique</h2>
    <p class="card-text">Lorem ipsum dolor sit amet, consectetur adipiscing elit. Curabitur et lectus vulputate, pharetra quam id, pharetra odio. Vestibulum eget enim vel quam.</p>
    <div class="card-more"><svg width="95" height="22" aria-hidden="true"><polygon points="18,0 95,0 95,22 0,22" fill="#0a76c4"/></svg><span>Lire la suite</span></div>
  </div>
  <div class="abs card" style="left:442px">
    <div class="card-media" role="img" aria-label="Homme d'affaires devant un tableau de croquis stratégiques" style="background:linear-gradient(135deg,#2d3138,#4a4f58 55%,#23262b)"></div>
    <h2 class="card-title"><b>Créativité</b> d'affaires</h2>
    <p class="card-text">Lorem ipsum dolor sit amet, consectetur adipiscing elit. Curabitur et lectus vulputate, pharetra quam id, pharetra odio. Vestibulum eget enim vel quam.</p>
    <div class="card-more"><svg width="95" height="22" aria-hidden="true"><polygon points="18,0 95,0 95,22 0,22" fill="#0a76c4"/></svg><span>Lire la suite</span></div>
  </div>
  <div class="abs card" style="left:743px">
    <div class="card-media" role="img" aria-label="Main sur une calculatrice au-dessus de graphiques financiers" style="background:linear-gradient(135deg,#dfe8f2,#f3f6fa 50%,#8aa6c4)"></div>
    <h2 class="card-title"><b>Développement des affaires</b> stratégique</h2>
    <p class="card-text">Lorem ipsum dolor sit amet, consectetur adipiscing elit. Curabitur et lectus vulputate, pharetra quam id, pharetra odio.</p>
    <div class="card-more"><svg width="95" height="22" aria-hidden="true"><polygon points="18,0 95,0 95,22 0,22" fill="#0a76c4"/></svg><span>Lire la suite</span></div>
  </div>

  <svg class="abs footer-shapes" width="1133" height="157" viewBox="0 0 1133 157" aria-hidden="true">
    <rect width="1133" height="157" fill="#333333"/>
    <polygon points="733,0 1133,0 1133,157 629,157" fill="#ffffff"/>
    <polygon points="741,0 1133,0 1133,157 637,157" fill="#0a76c4"/>
  </svg>

  <div class="abs f-head" style="left:142px">Plan du site</div>
  <ul class="abs f-list" style="left:142px">
    <li>Accueil</li><li>À propos</li><li>Services</li><li>Témoignages</li><li>Contact</li>
  </ul>

  <div class="abs f-head" style="left:309px">Nous joindre</div>
  <div class="abs f-row" style="left:305px;top:1084px">
    <svg width="13" height="12" viewBox="0 0 13 12" aria-hidden="true"><path d="M6.5 0 L13 6 L11 6 L11 12 L8 12 L8 8 L5 8 L5 12 L2 12 L2 6 L0 6 Z" fill="#9a9a9a"/></svg>
    <span>Lorem ipsum, dolor sit amet,<br>Consectetur lectus.</span>
  </div>
  <div class="abs f-row" style="left:306px;top:1118px">
    <svg width="12" height="14" viewBox="0 0 18 20" aria-hidden="true"><path d="M4 1 L7 5 L5 7 C6 10 8 13 11 15 L13 13 L17 16 L15 19 C8 18 2 11 1 4 Z" fill="#9a9a9a"/></svg>
    <span>514 555 0192</span>
  </div>
  <div class="abs f-row" style="left:327px;top:1143px"><span>info@lumivanconseil.ca</span></div>

  <div class="abs f-head" style="left:539px">Suivez-moi</div>
  <div class="abs f-row" style="left:540px;top:1087px"><span class="soc"></span><span>Suivez-moi sur<br><b>Pagewall</b></span></div>
  <div class="abs f-row" style="left:540px;top:1122px"><span class="soc"></span><span>Joignez-moi sur<br><b>Proflink</b></span></div>

  <div class="abs f-brand"><span class="brand-dot"></span>Lumivan Conseil</div>
  <div class="abs copyright">© Lumivan Conseil 2013. Tous droits réservés</div>
</div>
</body>
</html>
```